StoneHarbor - Business Card and Letterhead

After having received some fantastic submissions in our recent logo design project, I would now like to extend our branding to letterheads and business cards.
StoneHarbor is a consulting service in the Construction Industry. We deal with both residential and commercial projects, and our clients include Architects, Builders, Tradespeople and Home Owners.
The designs should be simple and effective, convey personal service and professionalism, and display some level of creativity.
For both the business cards and letterhead, a white card stock will be used. This project is for business cards and letterheads only. Our new logo is attached for use.
The designs should incorporate our two main colours which are Blue (RGB 14,92,143) and Green (RGB 132,194,37).
For the time being, please submit all designs showing generic information including name, mobile number, email, postal address and website details. No fax number or physical address is required. I will provide our actual contact details once a final design has been selected.
I encourage you to interpret this brief in your own creative way, and look forward to some quality submissions.
Thanks!
Lee
StoneHarbor.

```html
<!DOCTYPE html>
<html lang="en">
<head>
<meta charset="UTF-8">
<title>StoneHarbor – Business Card</title>
<link rel="stylesheet" href="https://fonts.googleapis.com/css2?family=Arimo:wght@400;700&display=swap">
<style>
  :root {
    --brand-blue: #3d5f96;
    --brand-green: #9bc54e;
    --steel: #a2b1cb;
    --pale-green: #d2e5b0;
    --mist: #f5f8ee;
    --frost: #e9edf3;
    --wave-green: #c9e19f;
    --ink: #111111;
    --slogan-grey: #7a7a7a;
    --address-green: #4c6a2a;
    --paper: #ffffff;
  }
  html, body {
    margin: 0;
    padding: 0;
    overflow: hidden;
    background: var(--paper);
  }
  .card {
    position: relative;
    width: 1200px;
    height: 750px;
    overflow: hidden;
    background: var(--paper);
    font-family: "Arimo", Arial, sans-serif;
    color: var(--ink);
  }
  .block { position: absolute; }
  .edge-blue   { left: 0; top: 0; width: 41px; height: 750px; background: var(--brand-blue); z-index: 3; }
  .edge-green  { right: 0; top: 0; width: 42px; height: 750px; background: var(--brand-green); z-index: 3; }
  .strip-green { left: 51px; top: 142px; width: 43px; height: 608px; background: var(--pale-green); z-index: 2; }
  .tint-top    { left: 41px; top: 0; width: 344px; height: 44px; background: var(--mist); }
  .tint-panel  { left: 101px; top: 144px; width: 284px; height: 284px; background: var(--mist); }
  .tint-square { left: 342px; top: 385px; width: 86px; height: 85px; background: var(--frost); }
  .steel-cap   { left: 1098px; top: 3px; width: 42px; height: 41px; background: var(--steel); }
  .steel-bar   { left: 1098px; top: 122px; width: 42px; height: 488px; background: var(--steel); }

  .waves {
    position: absolute;
    left: 0;
    top: 0;
    width: 1200px;
    height: 750px;
    z-index: 1;
  }

  .holder {
    position: absolute;
    left: 53px;
    top: 54px;
    font-size: 28px;
    line-height: 38px;
    z-index: 4;
  }
  .contact {
    position: absolute;
    right: 60px;
    top: 46px;
    text-align: right;
    font-size: 28px;
    line-height: 38px;
    z-index: 4;
  }

  .brand {
    position: absolute;
    left: 440px;
    top: 290px;
    width: 640px;
    text-align: center;
    z-index: 4;
  }
  .brand-name {
    display: block;
    font-size: 78px;
    font-weight: 700;
    letter-spacing: -1px;
    line-height: 90px;
    color: var(--brand-blue);
  }
  .brand-slogan {
    display: block;
    margin-top: 16px;
    font-size: 30px;
    letter-spacing: 0.2em;
    color: var(--slogan-grey);
  }

  .address {
    position: absolute;
    left: 94px;
    right: 42px;
    bottom: 10px;
    text-align: center;
    font-size: 20px;
    color: var(--address-green);
    z-index: 4;
  }
</style>
</head>
<body>
  <main class="card">
    <div class="block tint-top"></div>
    <div class="block tint-panel"></div>
    <div class="block tint-square"></div>
    <div class="block edge-blue"></div>
    <div class="block strip-green"></div>
    <div class="block steel-cap"></div>
    <div class="block steel-bar"></div>
    <div class="block edge-green"></div>

    <svg class="waves" viewBox="0 0 1200 750" aria-hidden="true">
      <path fill="var(--wave-green)" d="M94,750 C300,705 700,690 1158,672 L1158,750 Z"/>
      <path fill="var(--steel)" d="M94,672 C160,630 270,622 420,630 C620,642 820,690 985,692 C820,700 620,678 430,664 C290,655 180,662 94,706 Z"/>
    </svg>

    <div class="holder">
      <div class="holder-name">NAME</div>
      <div class="holder-role">Designation</div>
    </div>

    <div class="contact">
      <div class="contact-email">email:aaaa@company.com</div>
      <div class="contact-phone">Ph: 00 000000000</div>
    </div>

    <div class="brand">
      <span class="brand-name">StoneHarbor</span>
      <span class="brand-slogan">COMPANY SLOGAN</span>
    </div>

    <p class="address">Address: dummy dummy, dummy dummy dummy dummy</p>
  </main>
</body>
</html>
```